Enterprise Business Application

We need a two sided brochure for our new application named The PIVOT Metrics™. This cloud-based application is designed to help clients assess, track and coach employee performance. Our patent pending algorithm allows users to prioritize attributes for competencies classified as knowledge, skill and ability. We enhance the traditional process by standardizing coaching and reducing the amount of time required to coach performance.

We would like the brochure layout and them to compliment the enhancements we are making to our website.

Target Market(s)

Performance Managers

Industry/Entity Type

Business Software

Font styles to use
Sans Serif

Colors
9bcb3c
abd037
cadf82
eaf2ce
ffc214
fece3e
0792cd
33a6d7
f37122

Requirements
Must have
• incorporate our logo and brand colors, clean UX design,
Should not have
• Exaggerated overly happy Stock Photos

```html
<!DOCTYPE html>
<html lang="en">
<head>
<meta charset="utf-8">
<title>The PIVOT Metrics™ Brochure</title>
<link href="https://fonts.googleapis.com/css2?family=Open+Sans:wght@400;600;700;800&family=Montserrat:wght@700;800&display=swap" rel="stylesheet">
<style>
:root{
  --green:#9bcb3c;--lime:#abd037;--pale-green:#cadf82;--mist:#eaf2ce;
  --yellow:#ffc214;--gold:#fece3e;--blue:#0792cd;--sky:#33a6d7;--orange:#f37122;
  --ink:#2b3540;--grey:#6b7580;--bg:#ffffff;--dark:#1f2a36;
}
*{margin:0;padding:0;box-sizing:border-box}
html,body{width:667px;height:1200px;overflow:hidden;background:var(--bg)}
body{font-family:"Open Sans",Arial,sans-serif;color:var(--ink);position:relative}
.spread{position:absolute;left:40px;width:587px;height:380px;display:flex;box-shadow:0 2px 8px rgba(0,0,0,.25)}
.spread--outer{top:12px}.spread--inner{top:408px}.spread--action{top:804px}
.page{position:relative;width:293.5px;height:380px;background:#fff;overflow:hidden}
.page+.page{border-left:1px solid #e2e6ea}
.tiny{font-size:5px;line-height:1.45;color:var(--grey)}
.waves{position:absolute;left:0;bottom:0;width:100%;height:44px}
.web{position:absolute;bottom:6px;left:0;width:100%;text-align:center;font-size:6px;color:#fff;font-weight:600;z-index:2}
.photo{position:absolute;background:linear-gradient(135deg,#8fb7cf,#3d6f93 55%,#23405a)}
.brand{display:flex;align-items:center;gap:6px;font-family:"Montserrat",sans-serif;font-weight:800;color:var(--blue)}
.brand-dot{width:26px;height:26px;border-radius:50%;background:var(--green);flex:none}

/* about / back page */
.about{position:absolute;top:0;left:0;width:100%;height:150px;background:linear-gradient(120deg,var(--blue),#0a6c9b);padding:12px 14px}
.about-photo{right:0;top:0;width:110px;height:150px;background:linear-gradient(160deg,#6fa6c6,#1c5d86);opacity:.85}
.about h3{position:relative;font-size:9px;color:var(--yellow);font-weight:800;margin-bottom:5px}
.about p{position:relative;width:165px;font-size:5px;line-height:1.5;color:#eaf6fc}
.back-brand{position:absolute;top:178px;left:0;width:100%;justify-content:center;font-size:12px}
.contact{position:absolute;top:232px;left:0;width:100%;text-align:center}
.contact h3{font-size:10px;color:var(--blue);font-weight:700;margin-bottom:4px}
.contact p{font-size:6px;color:var(--grey);line-height:1.6}

/* cover */
.cover-brand{position:absolute;top:12px;left:16px;font-size:10px}
.cover-photo{left:0;top:46px;width:100%;height:160px;background:linear-gradient(135deg,#d9e6ee,#7aa7c4 50%,#2f5f82)}
.cover-band{position:absolute;top:196px;left:0;width:100%;height:30px}
.cover h1{position:absolute;top:236px;left:0;width:100%;text-align:center;font-family:"Montserrat",sans-serif;font-size:22px;font-weight:800;color:var(--blue)}
.cover-lede{position:absolute;top:272px;left:18px;width:258px;padding:6px 8px;background:var(--blue);color:#fff;font-size:5.5px;line-height:1.5;text-align:center}

/* inner */
.inner-pad{position:absolute;top:14px;left:14px;right:14px}
.sec-title{font-size:8px;font-weight:800;color:var(--blue);margin-bottom:5px;letter-spacing:.2px}
.sec-title::after{content:"";display:block;width:40px;height:2px;background:var(--green);margin-top:3px}
.label{display:block;margin:6px 0 3px;padding:2px 5px;font-size:6px;font-weight:700;color:#fff;background:var(--green)}
.label--blue{background:var(--blue)}
.bullets{list-style:none}
.bullets li{font-size:5px;line-height:1.45;color:var(--grey);padding-left:7px;position:relative}
.bullets li::before{content:"";position:absolute;left:0;top:2px;width:3px;height:3px;background:var(--green);border-radius:50%}
.welcome-photo{left:14px;top:282px;width:110px;height:62px}
.welcome-note{position:absolute;top:286px;left:132px;width:146px}
.solution{display:flex;gap:6px;margin-bottom:8px}
.icon{width:22px;height:22px;flex:none;display:flex;align-items:center;justify-content:center}
.icon--orange{background:var(--orange)}.icon--green{background:var(--green)}.icon--blue{background:var(--blue)}
.solution h4{font-size:6px;color:var(--blue);font-weight:700;margin-bottom:2px}
.clients{position:absolute;top:222px;left:14px;width:265px;height:90px;background:var(--dark);padding:0}
.clients h4{background:var(--green);color:#fff;font-size:6.5px;font-weight:800;padding:3px 8px;text-align:right}
.clients .bullets{position:absolute;left:100px;top:20px;width:158px}
.clients .bullets li{color:#dfe6ec}
.tablet{left:8px;top:18px;width:84px;height:64px;background:linear-gradient(135deg,#e9eef2,#9fb6c6)}

/* action */
.action-text{font-size:4.8px;line-height:1.45;color:var(--grey)}
.devices{left:18px;top:40px;width:258px;height:150px;background:linear-gradient(135deg,#f1f4f7,#b8c7d3 60%,#6f8aa0)}
.action-note{position:absolute;top:204px;left:18px;width:258px;text-align:center}
</style>
</head>
<body>

<!-- Outer spread: back panel and cover -->
<section class="spread spread--outer">
  <div class="page">
    <div class="about">
      <div class="photo about-photo" role="img" aria-label="Photo of a team working at an office desk"></div>
      <h3>ABOUT US</h3>
      <p>The PIVOT Metrics™ grew from one simple idea: clear, fair feedback helps every employee grow. Our cloud tool gives managers a steady way to assess, track and coach performance across every team, so reviews take less time and deliver more value to people and leaders.</p>
    </div>
    <div class="brand back-brand"><span class="brand-dot"></span>The PIVOT Metrics™</div>
    <div class="contact">
      <h3>Contact Us</h3>
      <p>hello@pivotmetrics.example<br>+1 555 014 2290</p>
    </div>
    <svg class="waves" viewBox="0 0 294 44" preserveAspectRatio="none" aria-hidden="true">
      <path d="M0 14 Q90 0 170 16 T294 10 V44 H0Z" fill="var(--green)"/>
      <path d="M0 24 Q100 10 190 26 T294 20 V44 H0Z" fill="var(--blue)"/>
    </svg>
    <div class="web">www.pivotmetrics.example</div>
  </div>

  <div class="page cover">
    <div class="brand cover-brand"><span class="brand-dot" style="width:18px;height:18px"></span>The PIVOT Metrics™</div>
    <div class="photo cover-photo" role="img" aria-label="Photo of a hand touching a glowing performance chart on a screen"></div>
    <svg class="cover-band" viewBox="0 0 294 30" preserveAspectRatio="none" aria-hidden="true">
      <path d="M0 10 Q150 -4 294 12 V30 H0Z" fill="var(--green)"/>
      <path d="M0 18 Q150 4 294 20 V30 H0Z" fill="#fff"/>
    </svg>
    <h1>YOU DESERVE TO KNOW</h1>
    <p class="cover-lede">The PIVOT Metrics™ is a cloud tool that helps you assess, track and coach employee performance with speed and clarity.</p>
    <svg class="waves" viewBox="0 0 294 44" preserveAspectRatio="none" aria-hidden="true">
      <path d="M0 14 Q90 0 170 16 T294 10 V44 H0Z" fill="var(--green)"/>
      <path d="M0 24 Q100 10 190 26 T294 20 V44 H0Z" fill="var(--blue)"/>
    </svg>
    <div class="web">www.pivotmetrics.example</div>
  </div>
</section>

<!-- Inner spread -->
<section class="spread spread--inner">
  <div class="page">
    <div class="inner-pad">
      <h2 class="sec-title">WELCOME TO THE PIVOT METRICS™</h2>
      <p class="tiny">With The PIVOT Metrics™ you can now set and track goals for employee development and performance in one simple place, then share clear insight with every manager.</p>
      <span class="label">Training</span>
      <p class="tiny">Provide role based training, measurable outcomes and steady progress reviews.</p>
      <span class="label">Development</span>
      <p class="tiny">Build each person's strengths, fill skill gaps and plan the next step.</p>
      <span class="label">Performance</span>
      <p class="tiny">Rank key attributes for every competency and coach performance against clear standards.</p>
      <ul class="bullets" style="margin-top:4px">
        <li>Track knowledge, skill and ability scores in one view.</li>
        <li>Spend less time per review with guided coaching steps.</li>
        <li>Share progress reports with leaders in one click.</li>
      </ul>
    </div>
    <div class="photo welcome-photo" role="img" aria-label="Photo of two colleagues reviewing results together"></div>
    <div class="welcome-note">
      <p class="tiny"><b style="color:var(--blue)">Measure the results that matter.</b> Guide each coaching talk with facts, not guesswork, and see growth over time.</p>
    </div>
    <svg class="waves" viewBox="0 0 294 44" preserveAspectRatio="none" aria-hidden="true" style="height:22px">
      <path d="M0 10 Q150 0 294 10 V44 H0Z" fill="var(--green)"/>
    </svg>
    <div class="web">www.pivotmetrics.example</div>
  </div>

  <div class="page">
    <div class="inner-pad">
      <h2 class="sec-title">EFFICIENT AND EFFECTIVE SOLUTIONS</h2>
      <div class="solution">
        <div class="icon icon--orange"><svg width="12" height="12" viewBox="0 0 12 12"><path d="M2 6l3 3 5-6" stroke="#fff" stroke-width="1.6" fill="none"/></svg></div>
        <div><h4>Performance Alignment</h4><p class="tiny">Link each goal to the skills and results your business needs most.</p></div>
      </div>
      <div class="solution">
        <div class="icon icon--green"><svg width="12" height="12" viewBox="0 0 12 12"><path d="M1 10h10M3 8V5M6 8V3M9 8V6" stroke="#fff" stroke-width="1.6"/></svg></div>
        <div><h4>Performance Coaching</h4><p class="tiny">Guided steps keep every coaching talk focused, fair and brief.</p></div>
      </div>
      <div class="solution">
        <div class="icon icon--blue"><svg width="12" height="12" viewBox="0 0 12 12"><circle cx="6" cy="6" r="4" stroke="#fff" stroke-width="1.6" fill="none"/><path d="M6 3.5V6l2 1" stroke="#fff" stroke-width="1.2" fill="none"/></svg></div>
        <div><h4>Performance Management</h4><p class="tiny">Track progress over time and spot trends before they become issues.</p></div>
      </div>
      <p class="tiny">The PIVOT Metrics™ offers a complete view of each employee so managers can act with confidence and teams know where they stand.</p>
    </div>
    <div class="clients">
      <h4>WHAT OUR CLIENTS GET</h4>
      <div class="photo tablet" role="img" aria-label="Illustration of a tablet showing a performance dashboard"></div>
      <ul class="bullets">
        <li>A clear scoring model for every role.</li>
        <li>Faster reviews with less paperwork.</li>
        <li>Consistent coaching across all teams.</li>
        <li>Reports that show real growth.</li>
      </ul>
    </div>
    <svg class="waves" viewBox="0 0 294 44" preserveAspectRatio="none" aria-hidden="true" style="height:22px">
      <path d="M0 10 Q150 0 294 10 V44 H0Z" fill="var(--green)"/>
    </svg>
    <div class="web">www.pivotmetrics.example</div>
  </div>
</section>

<!-- Action spread -->
<section class="spread spread--action">
  <div class="page">
    <div class="inner-pad">
      <h2 class="sec-title">SEE IT IN ACTION</h2>
      <span class="label label--blue">Comprehensive Performance Dashboard</span>
      <p class="action-text">See every score, goal and coaching note in one live view built for busy managers.</p>
      <span class="label label--blue">Employee Profiles</span>
      <p class="action-text">Each profile holds role, skills, history and current goals for quick reference.</p>
      <span class="label label--blue">Custom Competency Library</span>
      <p class="action-text">Build competencies for your roles and rank the attributes that matter most.</p>
      <span class="label label--blue">Guided Coaching Sessions</span>
      <p class="action-text">Step by step prompts help managers deliver clear, useful feedback every time.</p>
      <span class="label label--blue">Custom Reports</span>
      <p class="action-text">Export results by team, role or period to share with leaders.</p>
      <span class="label label--blue">Gap Analysis</span>
      <p class="action-text">Compare current scores with targets and plan training where it counts.</p>
    </div>
    <svg class="waves" viewBox="0 0 294 44" preserveAspectRatio="none" aria-hidden="true" style="height:22px">
      <path d="M0 10 Q150 0 294 10 V44 H0Z" fill="var(--green)"/>
    </svg>
    <div class="web">www.pivotmetrics.example</div>
  </div>

  <div class="page">
    <div class="photo devices" role="img" aria-label="Illustration of the dashboard shown on a monitor, laptop, tablet and phone"></div>
    <div class="action-note">
      <p class="tiny">Use it on any device. Your data stays secure in the cloud and ready whenever you need it, at the desk or on the move.</p>
    </div>
    <svg class="waves" viewBox="0 0 294 44" preserveAspectRatio="none" aria-hidden="true">
      <path d="M0 14 Q90 0 170 16 T294 10 V44 H0Z" fill="var(--green)"/>
      <path d="M0 24 Q100 10 190 26 T294 20 V44 H0Z" fill="var(--blue)"/>
    </svg>
    <div class="web">www.pivotmetrics.example</div>
  </div>
</section>

</body>
</html>
```